Handy man Company business card

need branded business card for my new company, this design will transfer to car wrap design what winner will be asked to design

I will need original file so I can edit it in the end.

Also like to have some inspirational quote like "ONE CALL WE DO IT ALL"
"We do it right" can be added to logo side

Like to try to see large 1 800 000 0000 number on front with large logo

Size bigger then standard business card

I like to integrate LAS VEGAS sign to one of sides

Target Market(s)

Handy man services, Home renovation and remodeling

Industry/Entity Type

Handyman

Contact Information for Business Card

Tool Baron LLC.
Name: BORIS LENKOVA
Phone "Temporary": 000 000 0000
Adress: 2715 Fenmore Ct, Las Vegas NV 89147
Website: www.toolbaron.vegas
Email: info@toolbaron.vegas

Requirements
Must have
• Two side
• side n1: LOGO
• side n2: INFO
Nice to have
• Like to have some interesting idea for client to remember!
• With logo added to both side at different stile
Should not have
• Standard design,

```html
<!DOCTYPE html>
<html lang="en">
<head>
<meta charset="UTF-8">
<title>Tool Baron – Business Card</title>
<link rel="stylesheet" href="https://fonts.googleapis.com/css2?family=Lato:wght@400;700&display=swap">
<style>
  :root {
    --page-bg: #f1f1f3;
    --navy: #1b2c3a;
    --amber: #e9a427;
    --white: #ffffff;
    --mascot-cap: #e9a427;
    --mascot-shirt: #8fd3f2;
  }
  * { margin: 0; padding: 0; box-sizing: border-box; }
  html, body {
    width: 1200px;
    height: 1200px;
    overflow: hidden;
    background: var(--page-bg);
    font-family: "Lato", sans-serif;
  }
  .card {
    position: absolute;
    top: 248px;
    width: 374px;
    height: 654px;
    background: var(--navy);
    overflow: hidden;
  }
  .card--info { left: 185px; }
  .card--logo { left: 663px; }

  .band {
    position: absolute;
    left: 0;
    width: 100%;
    background: var(--amber);
  }
  .card--info .band { top: 262px; height: 128px; }
  .card--logo .band { top: 298px; height: 128px; }

  .mascot {
    position: absolute;
    border-radius: 70px 70px 12px 12px;
    background: linear-gradient(180deg, var(--mascot-cap) 0%, var(--mascot-shirt) 45%, var(--mascot-cap) 70%, var(--mascot-cap) 100%);
    opacity: 0.9;
  }
  .card--info .mascot { left: 126px; top: 34px; width: 124px; height: 262px; }
  .card--logo .mascot { left: 140px; top: 130px; width: 98px; height: 202px; }

  .brand-name {
    position: absolute;
    left: 0;
    width: 100%;
    text-align: center;
    color: var(--white);
    font-weight: 700;
    line-height: 1;
  }
  .card--info .brand-name { top: 306px; font-size: 48px; }
  .card--logo .brand-name { top: 350px; font-size: 42px; }

  .name-strip {
    position: absolute;
    top: 390px;
    left: 0;
    width: 100%;
    height: 68px;
    background: var(--page-bg);
    display: flex;
    align-items: center;
    justify-content: center;
  }
  .person-name {
    color: var(--amber);
    font-weight: 700;
    font-size: 30px;
    letter-spacing: 0.3px;
  }

  .contact {
    position: absolute;
    top: 498px;
    left: 0;
    width: 100%;
    list-style: none;
    text-align: center;
    color: var(--white);
    font-size: 15px;
    letter-spacing: 0.8px;
  }
  .contact li { line-height: 24px; }
  .contact li:nth-child(n+3) { line-height: 22px; }
</style>
</head>
<body>
  <section class="card card--info">
    <div class="mascot" role="img" aria-label="Cartoon handyman mascot in cap and overalls holding a hammer, giving a thumbs up"></div>
    <div class="band"></div>
    <div class="brand-name">Tool Baron</div>
    <div class="name-strip"><h1 class="person-name">BORIS LENKOVA</h1></div>
    <ul class="contact">
      <li>000 000 0000</li>
      <li>2715 Fenmore Ct, Las Vegas NV 89147</li>
      <li>www.toolbaron.vegas</li>
      <li>info@toolbaron.vegas</li>
    </ul>
  </section>

  <section class="card card--logo">
    <div class="band"></div>
    <div class="mascot" role="img" aria-label="Cartoon handyman mascot in cap and overalls holding a hammer, giving a thumbs up"></div>
    <div class="brand-name">Tool Baron</div>
  </section>
</body>
</html>
```